Borvix Letter head

Borvix is a young and energetic software development consultancy. We spend our time working with clients to turn what ever is in their heads in to software.
We are trying to create an image of a high class software boutique who build class leading bespoke solutions.
We need a sharp letter head that looks great on high quality media.
We like bold colours and distinctive design. So show us what you can do.
Industry/Entity Type
Software
Requirements
Must have
- Our company is based in the UK and are requried to have on the paper somewhere the following information:
* Registered company name: Borvix Ltd
* Registered company number
* VAT registration number
In addition we also want the following:
* An email address
* Telephone number
* Website address
An example of what some pages have in their footer is something like the following:
Borvix Ltd is registered in England and Wales. Reg. no: 4916275
Registered office: 48 Quillmore Road, Harwick Dunshire, HR43PL. Tel: 07442615093
You do not have to use this sentance but please make sure your design incorporates accommodates the requirements for UK based companies

```html
<!DOCTYPE html>
<html lang="en">
<head>
<meta charset="utf-8">
<title>Borvix Stationery</title>
<link href="https://fonts.googleapis.com/css2?family=Open+Sans:wght@400;600;700&display=swap" rel="stylesheet">
<style>
  :root {
    --backdrop: #ececec;
    --paper: #ffffff;
    --brand-red: #c0161f;
    --ink: #3a3a3a;
    --ink-soft: #555555;
    --white: #ffffff;
  }
  * { margin: 0; padding: 0; box-sizing: border-box; }
  html, body {
    width: 1200px; height: 1086px; overflow: hidden;
    background: var(--backdrop);
    font-family: "Open Sans", Arial, sans-serif;
    color: var(--ink);
  }
  .canvas { position: relative; width: 1200px; height: 1086px; }

  .letterhead {
    position: absolute; left: 60px; top: 71px; width: 733px; height: 943px;
    background: var(--paper);
    border-radius: 0 30px 0 30px;
  }
  .wordmark {
    display: flex; align-items: center; gap: 6px;
    font-weight: 700; letter-spacing: 1px; line-height: 1;
    color: var(--brand-red);
  }
  .wordmark .mark-square {
    width: 0.7em; height: 0.7em; background: currentColor;
  }
  .letterhead .wordmark {
    position: absolute; left: 534px; top: 67px; font-size: 25px;
  }
  .contact {
    font-size: 8.4px; line-height: 9.6px; color: var(--ink-soft);
  }
  .contact .label { color: var(--brand-red); font-weight: 600; margin-right: 3px; }
  .contact .group + .group { margin-top: 6px; }
  .letterhead .contact { position: absolute; left: 534px; top: 105px; }

  .card {
    position: absolute; left: 842px; width: 298px; height: 170px;
    border-radius: 0 16px 0 16px;
  }
  .card-front { top: 356px; background: var(--paper); }
  .card-front .wordmark { position: absolute; left: 155px; top: 34px; font-size: 19px; }
  .card-front .holder {
    position: absolute; left: 32px; top: 87px;
    font-size: 9.5px; font-weight: 700; color: var(--ink);
  }
  .card-front .contact {
    position: absolute; left: 155px; top: 88px;
    font-size: 6.6px; line-height: 8.6px;
  }
  .card-front .company { color: var(--brand-red); font-weight: 600; }

  .card-back {
    top: 559px; background: var(--brand-red); color: var(--white);
    display: flex; flex-direction: column; align-items: center; justify-content: center;
  }
  .card-back .wordmark { color: var(--white); font-size: 25px; margin-top: 4px; }
  .card-back .website {
    margin-top: 22px; font-size: 6.5px; font-weight: 600; letter-spacing: 1.4px;
  }
</style>
</head>
<body>
<main class="canvas">
  <section class="letterhead" aria-label="Letterhead">
    <div class="wordmark"><span class="mark-square"></span>BORVIX</div>
    <div class="contact">
      <div class="group">48 Quillmore Road, Harwick<br>Dunshire HR4 3PL</div>
      <div class="group">
        <div><span class="label">Phone</span>07442 615093</div>
        <div><span class="label">Email</span>dcarver@borvix.com</div>
        <div><span class="label">Reg. #</span>4916275</div>
      </div>
    </div>
  </section>

  <section class="card card-front" aria-label="Business card front">
    <div class="wordmark"><span class="mark-square"></span>BORVIX</div>
    <div class="holder">Daniel Carver</div>
    <div class="contact">
      <div class="group">
        <div class="company">Borvix Ltd</div>
        <div>48 Quillmore Road, Harwick</div>
        <div>Dunshire HR4 3PL</div>
      </div>
      <div class="group">
        <div><span class="label">Phone</span>07442 615093</div>
        <div><span class="label">Email</span>dcarver@borvix.com</div>
        <div><span class="label">Reg. #</span>4916275</div>
      </div>
    </div>
  </section>

  <section class="card card-back" aria-label="Business card back">
    <div class="wordmark"><span class="mark-square"></span>BORVIX</div>
    <div class="website">www.borvix.com</div>
  </section>
</main>
</body>
</html>
```